Ashcombe TIMES: Final product due on March 4, 2019

We need a newspaper ad for a retirement community called "Orla Penn" located in Manteca, CA. We are estate planning law firm. We would like to include our logo (either blue or white background one) and contents attached (we are flexible to reduce a number of characters), as well as our photo (w/ white background) that will be sent later. We would like to see designs that draw attentions from senior people. You are free to be creative!
Size: 10” wide x 5.5” high
Specs: Artwork must be provided electronically in a pdf format. Color ads must be provided in a color format.

Target Market(s)

Active retirement community in Manteca, CA

Industry/Entity Type

Law Firm

Colors

Designer to choose colors to be used in the design.

Requirements
Must have
• Our logo and contents - see attachments.
• Our photo to be sent tomorrow.
Nice to have
• Use good colors for newspaper ad.
• You are free to be creative.

```html
<!DOCTYPE html>
<html lang="en">
<head>
<meta charset="utf-8">
<title>Forward Planning – Newspaper Ad</title>
<link rel="stylesheet" href="https://fonts.googleapis.com/css2?family=Anton&family=Lato:ital,wght@0,400;0,700;0,900;1,400;1,700&display=swap">
<style>
  :root {
    --page: #1f1f1f;
    --brand-blue: #0755a5;
    --brand-yellow: #fdd400;
    --paper: #ffffff;
    --ink: #111111;
    --photo-light: #b88a4a;
    --photo-mid: #5a4330;
    --photo-dark: #1c1714;
  }
  html, body {
    margin: 0;
    width: 1200px;
    height: 1200px;
    overflow: hidden;
    background: var(--page);
  }
  .ad {
    position: absolute;
    left: 104px;
    top: 314px;
    width: 1248px;
    height: 688px;
    transform: scale(0.8);
    transform-origin: 0 0;
    overflow: hidden;
    background: var(--brand-blue);
    font-family: "Lato", sans-serif;
    box-shadow: 0 10px 30px rgba(0,0,0,.5);
  }
  .ad__shapes { position: absolute; inset: 0; }
  .ad__title {
    position: absolute;
    left: 48px;
    top: 40px;
    margin: 0;
    font-family: "Anton", sans-serif;
    font-weight: 400;
    font-size: 70px;
    line-height: 68px;
    color: var(--paper);
    letter-spacing: 0.5px;
  }
  .ad__body {
    position: absolute;
    left: 23px;
    top: 278px;
    width: 656px;
    color: var(--ink);
    font-size: 15px;
    line-height: 19px;
  }
  .ad__body p { margin: 0 0 12px; }
  .ad__lead { font-size: 17.5px; line-height: 22px; margin-bottom: 4px !important; }
  .ad__quote {
    width: 640px;
    font-style: italic;
    font-size: 18.5px;
    line-height: 23px;
  }
  .ad__brand {
    position: absolute;
    left: 800px;
    top: 538px;
    width: 400px;
    text-align: center;
    color: var(--paper);
    font-weight: 700;
    font-size: 33px;
    letter-spacing: 2px;
  }
  .contact {
    position: absolute;
    display: flex;
    align-items: center;
    gap: 12px;
    color: var(--paper);
    font-size: 19.5px;
  }
  .contact svg { flex: none; }
  .contact--address { left: 28px; top: 628px; line-height: 23px; }
  .contact--address strong { display: block; font-weight: 700; }
  .contact--phone { left: 596px; top: 644px; font-weight: 700; font-size: 20px; }
  .contact--web { left: 885px; top: 645px; font-weight: 700; font-size: 20px; }
</style>
</head>
<body>
<article class="ad">
  <svg class="ad__shapes" viewBox="0 0 1248 688" width="1248" height="688">
    <defs>
      <radialGradient id="photoTone" cx="0.3" cy="0.35" r="0.8">
        <stop offset="0" stop-color="var(--photo-light)"/>
        <stop offset="0.45" stop-color="var(--photo-mid)"/>
        <stop offset="1" stop-color="var(--photo-dark)"/>
      </radialGradient>
    </defs>
    <!-- top yellow swoosh -->
    <path d="M0,158 C180,240 400,255 560,210 L720,140 L720,320 L0,320 Z" fill="var(--brand-yellow)"/>
    <!-- white content panel -->
    <path d="M0,223 C200,275 450,262 706,148 L1000,148 L1000,600 L0,600 Z" fill="var(--paper)"/>
    <!-- photo frame: yellow ring, blue ring, photo -->
    <g>
      <circle cx="990" cy="250" r="302" fill="var(--brand-yellow)"/>
      <rect x="990" y="0" width="258" height="688" fill="var(--brand-yellow)"/>
      <circle cx="990" cy="250" r="292" fill="var(--brand-blue)"/>
      <rect x="990" y="0" width="258" height="688" fill="var(--brand-blue)"/>
      <g role="img" aria-label="Photo of a bronze statue of Lady Justice holding scales">
        <circle cx="990" cy="250" r="280" fill="url(#photoTone)"/>
        <rect x="990" y="0" width="258" height="688" fill="url(#photoTone)"/>
      </g>
    </g>
    <!-- bottom yellow swoosh -->
    <path d="M0,548 C250,615 520,600 720,555 L720,688 L0,688 Z" fill="var(--brand-yellow)"/>
    <!-- bottom blue wave -->
    <path d="M0,583 C200,630 450,625 640,575 C720,552 760,522 800,505 C880,478 960,460 1030,462 C1130,466 1200,490 1248,513 L1248,688 L0,688 Z" fill="var(--brand-blue)"/>
  </svg>

  <h1 class="ad__title">Forward Planning<br>A Law Corporation</h1>

  <div class="ad__body">
    <p class="ad__lead">Taking care of your family, finances, and healthcare is so vitally important.</p>
    <p>ATTORNEY MARCUS HALE has helped hundreds of Sacramento and Manteca area residents protect themselves and their families. We are located in a convenient location in Manteca— just on the corner of Elm and Harbor, <strong>ONLY A SEVEN MINUTE DRIVE FROM ORLA PENN!</strong> We also do house calls!</p>
    <p>An attorney widely trusted by the Orla Penn Community! See what previous clients have to say about me! I have a 10/10 score on Lexrate, have been selected as a “Rising Star” by Counsel Stars, and have been selected as one of the Top 20 Estate Planning Attorneys in Sacramento by Advisorly.com.</p>
    <p class="ad__quote">“What we like the best is there is never a cost to speak with Marcus about our estate plan. We got all our questions answered and had great peace of mind after working with him!” <strong>– Nolan &amp; Reva</strong></p>
  </div>

  <div class="ad__brand">FORWARD PLANNING</div>

  <div class="contact contact--address">
    <svg width="20" height="26" viewBox="0 0 20 26" aria-hidden="true"><path d="M10 1a8 8 0 0 0-8 8c0 6 8 15 8 15s8-9 8-15a8 8 0 0 0-8-8z" fill="var(--brand-yellow)"/><circle cx="10" cy="9" r="3.2" fill="var(--brand-blue)"/></svg>
    <span><strong>Estate Planning Law Firm</strong>2480 North Elm Avenue | Suite #210 | Manteca CA 95336</span>
  </div>

  <div class="contact contact--phone">
    <svg width="32" height="32" viewBox="0 0 32 32" aria-hidden="true"><circle cx="16" cy="16" r="14" fill="none" stroke="var(--brand-yellow)" stroke-width="2"/><path d="M11 9l3 3-2 2c1 2 3 4 5 5l2-2 3 3-2 2c-5 0-11-6-11-11z" fill="var(--brand-yellow)"/></svg>
    <span>(209) 555-0148</span>
  </div>

  <div class="contact contact--web">
    <svg width="28" height="28" viewBox="0 0 28 28" aria-hidden="true" fill="none" stroke="var(--brand-yellow)" stroke-width="1.8"><circle cx="14" cy="14" r="12"/><ellipse cx="14" cy="14" rx="5" ry="12"/><path d="M2 14h24M4 8h20M4 20h20"/></svg>
    <span>www.forwardplanninglaw.com</span>
  </div>
</article>
</body>
</html>
```